Modernization of existing web site

Update existing web site to a professional look vs a home-made site. Site look and navigation should be up to today's standards and display properly on mobile devices.
Only simple HTML and CSS is to be used as this is a basic site. No content management.
Existing site is https://www.plinvaro.example

Target Market(s)

Insurance and Technology

Industry/Entity Type

Insurance and technology

Coding

Coded - Design and coding required

Number of Pages Required

5+ page

Font styles to use
Sans Serif

Colors
0054AA
0677BA
7BADD7
CADEEF
E8F1F8
0094D4
00A9DD
6FCCEA
C7EBF8
E9F6FB

Requirements
Must have
• A sleek, modern feel and also done with a button-downed industry in mind.
Nice to have
• Clean integration of the logo and name
Should not have
• Open to ideas

```html
<!DOCTYPE html>
<html lang="en">
<head>
<meta charset="utf-8">
<title>Plinvaro — Navigating Business and Technology</title>
<link rel="stylesheet" href="https://fonts.googleapis.com/css2?family=Montserrat:wght@600;700;800&family=Roboto:wght@400;500;700&display=swap">
<style>
:root{
  --navy:#1f3c96;
  --navy-dark:#0d1f4a;
  --blue:#2a78c2;
  --orange:#f7941d;
  --ink:#222;
  --body:#555;
  --muted:#777;
  --grey:#555a60;
  --pale:#eaf0fa;
  --line:#d6dbe3;
  --white:#fff;
  --black:#0a0a0a;
}
*{box-sizing:border-box;margin:0;padding:0}
html,body{width:1200px;height:4193px;overflow:hidden}
body{font-family:"Roboto",Arial,sans-serif;color:var(--body);background:var(--white);position:relative}
.abs{position:absolute}
h1,h2,h3,.heading{font-family:"Montserrat",Arial,sans-serif}
.btn{position:absolute;display:flex;align-items:center;justify-content:center;gap:8px;font-family:"Roboto",Arial,sans-serif;font-weight:700;font-size:14px;color:var(--white);text-transform:uppercase;border-radius:3px}
.btn-orange{background:var(--orange)}
.btn-navy{background:var(--navy)}
.btn .arrow{width:13px;height:13px;border-radius:50%;background:var(--white);display:inline-block;position:relative}
.btn .arrow::after{content:"";position:absolute;left:4px;top:3.5px;border-left:5px solid currentColor;border-top:3px solid transparent;border-bottom:3px solid transparent;filter:none}
.btn-orange .arrow::after{border-left-color:var(--orange)}
.btn-navy .arrow::after{border-left-color:var(--navy)}
.rule{position:absolute;height:3px;width:46px;background:var(--orange)}

/* header */
.topbar{left:480px;top:0;width:720px;height:44px;background:var(--grey);clip-path:polygon(0 0,100% 0,100% 100%,40px 100%)}
.topbar .contact{position:absolute;top:0;height:44px;display:flex;align-items:center;gap:10px;color:var(--white);font-size:14px}
.topbar .ico{width:26px;height:26px;border-radius:50%;border:1.5px solid var(--white);display:flex;align-items:center;justify-content:center}
.brand{left:111px;top:34px;font-family:"Montserrat",Arial,sans-serif;font-weight:800;font-size:40px;color:var(--navy);letter-spacing:.5px}
.nav a{position:absolute;top:72px;font-size:15px;font-weight:500;color:var(--ink);text-decoration:none}
.nav a.active{color:var(--navy)}

/* hero */
.hero{left:0;top:120px;width:1200px;height:770px;background:radial-gradient(circle at 78% 40%,#3a6aa8 0%,#143a72 35%,#0b2148 70%,#081733 100%)}
.hero-text{left:111px;color:var(--white)}
.hero .kicker{top:200px;font-size:36px;font-weight:700;letter-spacing:1px}
.hero .title{top:245px;font-size:96px;font-weight:800;letter-spacing:2px;line-height:1.1}
.hero .lead{top:362px;width:520px;font-size:18px;font-weight:500;line-height:1.45}

/* intro */
.intro-img{left:111px;top:895px;width:462px;height:416px;background:radial-gradient(circle at 55% 50%,#6cb3ea 0%,#1f5fb0 40%,#0b2a6a 100%)}
.intro h2{left:648px;top:905px;width:480px;font-size:32px;font-weight:700;line-height:1.22;color:var(--navy)}
.intro p{left:648px;top:1065px;width:446px;font-size:14px;line-height:24px;color:var(--body);text-align:justify}

/* offer */
.section-title{left:0;width:1200px;text-align:center;font-size:32px;font-weight:700;color:var(--navy)}
.card{top:1500px;width:391px;height:387px;overflow:hidden}
.card .photo{position:absolute;inset:0}
.card .band{position:absolute;left:0;bottom:0;width:100%;height:92px;background:var(--navy);clip-path:polygon(0 30%,100% 0,100% 100%,0 100%)}
.card .label{position:absolute;left:0;bottom:18px;width:100%;text-align:center;font-family:"Montserrat",Arial,sans-serif;font-weight:700;font-size:28px;color:var(--white)}
.card.tech{background:var(--navy);color:var(--white);text-align:center}
.card.tech h3{margin-top:68px;font-size:28px;font-weight:700}
.card.tech .rule{left:172px;top:122px}
.card.tech p{margin:40px 24px 0;font-size:15px;line-height:24px;text-align:justify}

/* services */
.services{left:0;top:1897px;width:1200px;height:760px;background:var(--pale)}
.svc-icon{position:absolute;width:72px;height:72px;border-radius:50%;background:var(--white);box-shadow:0 4px 10px rgba(31,60,150,.18);display:flex;align-items:center;justify-content:center}
.svc-label{position:absolute;font-size:17px;color:#4a4f57;line-height:22px}
.hub{position:absolute;left:488px;top:278px;width:238px;height:238px;border-radius:50%;background:var(--navy);display:flex;align-items:center;justify-content:center;color:var(--white);font-family:"Montserrat",Arial,sans-serif;font-weight:800;font-size:30px;letter-spacing:1px}

/* about */
.about h2{left:111px;top:2745px;font-size:32px;font-weight:700;color:var(--navy)}
.about p{position:absolute;left:111px;width:446px;font-size:14px;line-height:24px;text-align:justify}
.portrait{left:661px;top:2755px;width:406px;height:406px;border-radius:50%;background:radial-gradient(circle at 50% 60%,#cfcfcf 0%,#8a8a8a 60%,#4a4a4a 100%)}

/* help */
.help{left:0;top:3253px;width:1200px;height:640px;background:linear-gradient(180deg,#2f7fc8 0%,#2a74bf 70%,#1f5fb0 100%)}
.help h2{color:var(--white)}
.field{position:absolute;background:var(--white);font-size:16px;color:#777;padding:0 20px;display:flex;align-items:center}
.field.area{align-items:flex-start;padding-top:15px}

/* footer */
.footer{left:0;top:3842px;width:1200px;height:351px;background:var(--black);color:var(--white)}
.footer h4{position:absolute;top:30px;font-family:"Roboto",Arial,sans-serif;font-weight:700;font-size:16px;text-decoration:underline}
.flinks{position:absolute;top:80px;list-style:none}
.flinks li{font-size:13px;height:34px;padding-left:24px;position:relative}
.flinks li::before{content:"»";position:absolute;left:0;top:-2px;color:var(--orange);font-size:15px}
.fc{position:absolute;display:flex;align-items:center;gap:18px;font-size:13px;line-height:20px}
.fc .dot{width:32px;height:32px;border-radius:50%;background:#3a2a14;display:flex;align-items:center;justify-content:center;flex:none}
.fdivider{position:absolute;left:111px;top:264px;width:978px;height:1px;background:#444}
.copy{position:absolute;top:298px;width:1200px;text-align:center;font-size:14px}
</style>
</head>
<body>

<!-- header -->
<div class="abs topbar">
  <div class="contact" style="left:172px">
    <span class="ico"><svg width="12" height="10" viewBox="0 0 12 10"><rect x="0.5" y="0.5" width="11" height="9" fill="#fff"/><path d="M0.5 0.5 6 5 11.5 0.5" stroke="#555a60" fill="none"/></svg></span>
    info@plinvaro.example
  </div>
  <div class="contact" style="left:362px;font-size:12px">|</div>
  <div class="contact" style="left:436px;font-size:19px;font-weight:700">
    <span class="ico"><svg width="12" height="12" viewBox="0 0 24 24"><path fill="#fff" d="M6.6 10.8a15 15 0 0 0 6.6 6.6l2.2-2.2a1 1 0 0 1 1-.25 11.4 11.4 0 0 0 3.6.57 1 1 0 0 1 1 1V20a1 1 0 0 1-1 1A17 17 0 0 1 3 4a1 1 0 0 1 1-1h3.5a1 1 0 0 1 1 1c0 1.25.2 2.45.57 3.57a1 1 0 0 1-.25 1z"/></svg></span>
    555-014-2290
  </div>
</div>
<div class="abs brand">PLINVARO</div>
<nav class="nav">
  <a class="active" style="left:423px">Home</a>
  <a style="left:495px">About Us</a>
  <a style="left:589px">Our Services</a>
  <a style="left:709px">Privacy Policy</a>
  <a style="left:837px">Contact Us</a>
</nav>
<a class="btn btn-navy" style="left:956px;top:62px;width:132px;height:40px;font-size:13px">Get Started <span class="arrow"></span></a>

<!-- hero -->
<section class="abs hero" role="img" aria-label="Hand launching a rocket surrounded by glowing technology icons on a deep blue background">
  <div class="abs hero-text kicker heading">WELCOME TO</div>
  <h1 class="abs hero-text title">PLINVARO</h1>
  <p class="abs hero-text lead">At PLINVARO, we are here to assist you in realizing your vision for your business.</p>
  <a class="btn btn-orange" style="left:111px;top:442px;width:143px;height:48px">Get Started <span class="arrow"></span></a>
  <svg class="abs" style="left:0;bottom:-2px" width="1200" height="240" viewBox="0 0 1200 240" preserveAspectRatio="none">
    <path d="M0 240 L0 190 C220 40 420 20 620 90 C820 160 1000 170 1200 80 L1200 240 Z" fill="#1f3c96"/>
    <path d="M0 240 L0 225 C230 70 430 60 640 130 C840 195 1030 200 1200 125 L1200 240 Z" fill="#ffffff"/>
    <path d="M780 170 C950 180 1080 140 1200 50 L1200 120 C1060 190 940 200 780 170 Z" fill="#555a60"/>
  </svg>
</section>

<!-- intro -->
<section class="intro">
  <div class="abs intro-img" role="img" aria-label="Glowing compass over a network of connected points"></div>
  <h2 class="abs">NAVIGATING BUSINESS AND TECHNOLOGY TO GENERATE RESULTS</h2>
  <div class="rule" style="left:648px;top:1040px"></div>
  <p class="abs">At PLINVARO, we are here to assist you in realizing your vision for your business.We offer a number of different services for insurance, technology, and financial services firms. We have extensive experience in many areas of business and technology combined with a deep level of integrity in the way we do business. If you have a specific need not mentioned on our website, contact us today with your details.</p>
  <a class="btn btn-orange" style="left:648px;top:1246px;width:144px;height:48px">Learn More <span class="arrow"></span></a>
</section>

<!-- offer -->
<h2 class="abs section-title" style="top:1400px">WHAT WE OFFER</h2>
<div class="rule" style="left:577px;top:1460px"></div>
<div class="abs card" style="left:0">
  <div class="photo" role="img" aria-label="Couple reviewing insurance papers with an advisor" style="background:linear-gradient(135deg,#e9e4dc,#b9a48c 55%,#6d5a49)"></div>
  <div class="band"></div><div class="label">Insurance</div>
</div>
<div class="abs card tech" style="left:404px">
  <h3>Technology</h3>
  <div class="rule"></div>
  <p>Lorem ipsum dolor sit amet, consectetur adipiscing elit, sed do eiusmod tempor incididunt ut labore et dolore magna aliqua. Ut enim ad minim veniam, quis nostrud exercitation ullamco laboris nisi ut aliquip ex ea commodo consequat. Duis aute irure dolor in reprehenderit in voluptate velit esse cillum dolore eu fugiat nulla pariatur.</p>
</div>
<div class="abs card" style="left:809px">
  <div class="photo" role="img" aria-label="Business team discussing financial charts in an office" style="background:linear-gradient(135deg,#dcdfe2,#9aa3aa 55%,#4b5560)"></div>
  <div class="band"></div><div class="label">Financial</div>
</div>

<!-- services -->
<section class="abs services">
  <h2 class="abs section-title" style="top:75px">OUR SERVICES</h2>
  <div class="rule" style="left:577px;top:133px"></div>
  <svg class="abs" style="left:0;top:0" width="1200" height="760" fill="none" stroke="#c9cfd8" stroke-width="2">
    <path d="M607 278 C607 230 607 210 607 184"/>
    <path d="M520 300 C480 260 460 270 433 271"/>
    <path d="M490 360 C450 360 420 359 393 359"/>
    <path d="M490 430 C450 440 420 447 393 447"/>
    <path d="M505 490 C470 520 455 530 438 535"/>
    <path d="M560 510 C545 550 540 570 541 587"/>
    <path d="M607 516 C600 560 610 600 615 626"/>
    <path d="M660 510 C690 560 700 580 724 589"/>
    <path d="M710 480 C760 520 790 530 819 538"/>
    <path d="M726 420 C800 430 830 440 876 447"/>
    <path d="M722 360 C780 350 820 351 861 351"/>
    <path d="M700 300 C740 265 780 262 811 262"/>
  </svg>
  <div class="hub">PLINVARO</div>

  <div class="svc-icon" style="left:571px;top:148px"><svg width="34" height="34" viewBox="0 0 24 24" fill="none" stroke="#1f3c96" stroke-width="2.2"><circle cx="13" cy="10" r="6"/><path d="M9 14 3 20"/></svg></div>
  <div class="svc-label" style="left:660px;top:173px">M &amp; A Due Diligence</div>

  <div class="svc-icon" style="left:361px;top:235px"><svg width="32" height="32" viewBox="0 0 24 24"><path fill="#1f3c96" d="M12 3 22 20H2z"/><rect x="11" y="9" width="2" height="6" fill="#fff"/><rect x="11" y="16" width="2" height="2" fill="#fff"/></svg></div>
  <div class="svc-label" style="left:96px;top:260px">Catastrophe Risk Management</div>

  <div class="svc-icon" style="left:321px;top:323px"><svg width="32" height="32" viewBox="0 0 24 24" fill="#1f3c96"><rect x="3" y="12" width="18" height="8" rx="1"/><path d="M4 10 12 4l8 6z"/></svg></div>
  <div class="svc-label" style="left:198px;top:348px">Reinsurance</div>

  <div class="svc-icon" style="left:321px;top:411px"><svg width="32" height="32" viewBox="0 0 24 24" fill="#1f3c96"><circle cx="12" cy="8" r="5"/><path d="M3 22c0-5 4-8 9-8s9 3 9 8z"/></svg></div>
  <div class="svc-label" style="left:126px;top:436px">Product Development</div>

  <div class="svc-icon" style="left:366px;top:499px"><svg width="32" height="32" viewBox="0 0 24 24"><circle cx="12" cy="12" r="8" fill="#1f3c96"/><circle cx="12" cy="12" r="3" fill="#fff"/></svg></div>
  <div class="svc-label" style="left:128px;top:524px">Technology Implementation</div>

  <div class="svc-icon" style="left:469px;top:551px"><svg width="30" height="30" viewBox="0 0 24 24" fill="#1f3c96"><rect x="3" y="4" width="8" height="17"/><rect x="13" y="9" width="8" height="12"/></svg></div>
  <div class="svc-label" style="left:247px;top:604px">Enterprise Risk Management</div>

  <div class="svc-icon" style="left:579px;top:590px"><svg width="30" height="30" viewBox="0 0 24 24" fill="#1f3c96"><rect x="3" y="8" width="18" height="12" rx="1"/><rect x="6" y="4" width="12" height="3"/></svg></div>
  <div class="svc-label" style="left:519px;top:677px">Data/Reporting/Analytics</div>

  <div class="svc-icon" style="left:688px;top:553px"><svg width="30" height="30" viewBox="0 0 24 24" fill="#1f3c96"><rect x="3" y="16" width="5" height="5"/><rect x="10" y="11" width="5" height="10"/><rect x="17" y="5" width="5" height="16"/></svg></div>
  <div class="svc-label" style="left:768px;top:605px">Interim Executive Leadership</div>

  <div class="svc-icon" style="left:783px;top:502px"><svg width="30" height="30" viewBox="0 0 24 24"><path fill="#1f3c96" d="M12 2 20 5v7c0 5-3.5 8.5-8 10-4.5-1.5-8-5-8-10V5z"/><path d="M8 12l3 3 5-6" stroke="#fff" stroke-width="2" fill="none"/></svg></div>
  <div class="svc-label" style="left:874px;top:535px">Insurance Operations/Process</div>

  <div class="svc-icon" style="left:840px;top:411px"><svg width="32" height="32" viewBox="0 0 24 24" fill="#1f3c96"><circle cx="12" cy="8" r="5"/><path d="M4 22l2-6h12l2 6z"/></svg></div>
  <div class="svc-label" style="left:941px;top:436px">Rating and Regulatory</div>

  <div class="svc-icon" style="left:825px;top:315px"><svg width="30" height="30" viewBox="0 0 24 24" fill="#1f3c96"><rect x="5" y="3" width="14" height="18" rx="1"/><path d="M9 10l-2 2 2 2M15 10l2 2-2 2" stroke="#fff" stroke-width="1.6" fill="none"/></svg></div>
  <div class="svc-label" style="left:924px;top:330px">Distribution Channel<br>Development</div>

  <div class="svc-icon" style="left:775px;top:226px"><svg width="32" height="32" viewBox="0 0 24 24"><circle cx="12" cy="12" r="9" fill="#1f3c96"/><path d="M7 13l3 3 7-7" stroke="#fff" stroke-width="2" fill="none"/></svg></div>
  <div class="svc-label" style="left:875px;top:248px">Business &amp; Technology<br>Strategy</div>
</section>

<!-- about -->
<section class="about">
  <h2 class="abs">ABOUT PLINVARO</h2>
  <div class="rule" style="left:111px;top:2805px"></div>
  <p style="top:2834px">Plinvaro was formed in late 2018 to bring over 35 years of experience in multiple industries and disciplines to our customers.</p>
  <p style="top:2906px">Dale Wexford has led large and small organizations. With senior executive experience in business and technology, he has a distinct view of the business and technology needs of organizations.</p>
  <p style="top:3002px">Dale has spent the last 20 years in various senior leadership positions at a leading property &amp; casualty insurance group, most recently as Chairman and President. He spent the early years of his career in high-tech manufacturing.</p>
  <a class="btn btn-orange" style="left:111px;top:3120px;width:144px;height:48px">Learn More <span class="arrow"></span></a>
  <div class="abs portrait" role="img" aria-label="Portrait of the company founder in a dark suit"></div>
</section>

<!-- help -->
<section class="abs help">
  <h2 class="abs section-title" style="top:48px;color:#fff">WE’RE HERE TO HELP</h2>
  <div class="rule" style="left:577px;top:103px;background:#fff"></div>
  <div class="field" style="left:111px;top:141px;width:462px;height:48px">Name</div>
  <div class="field" style="left:111px;top:202px;width:462px;height:48px">Company</div>
  <div class="field" style="left:111px;top:262px;width:462px;height:48px">Email</div>
  <div class="field" style="left:111px;top:322px;width:462px;height:48px">Subject</div>
  <div class="field area" style="left:585px;top:141px;width:504px;height:168px">How can we help you?</div>
  <a class="btn btn-navy" style="left:946px;top:322px;width:143px;height:48px">Submit Now</a>
</section>

<svg class="abs" style="left:0;top:3620px" width="1200" height="240" viewBox="0 0 1200 240" preserveAspectRatio="none">
  <path d="M0 240 L0 120 C200 40 450 40 640 140 C820 230 1000 160 1200 40 L1200 240 Z" fill="#0a0a0a"/>
  <path d="M0 150 C150 70 340 60 640 210 C380 110 180 110 0 200 Z" fill="#555a60"/>
  <path d="M760 160 C900 150 1060 90 1200 20 L1200 50 C1060 130 900 180 760 160 Z" fill="#1f3c96"/>
</svg>

<!-- footer -->
<footer class="abs footer">
  <h4 style="left:111px">Quick Links</h4>
  <ul class="flinks" style="left:111px"><li>Home</li><li>Our Services</li><li>About Us</li><li>Contact Us</li><li>Privacy Policy</li></ul>
  <h4 style="left:334px">Other Links</h4>
  <ul class="flinks" style="left:334px"><li>FAQ</li><li>Privacy Policy</li><li>Terms Of Use</li><li>Help Of Service</li><li>Reviews</li></ul>
  <h4 style="left:550px">Neem Contact Op</h4>
  <div class="fc" style="left:550px;top:72px">
    <span class="dot"><svg width="12" height="14" viewBox="0 0 24 28"><path fill="#f7941d" d="M12 0a10 10 0 0 0-10 10c0 7 10 18 10 18s10-11 10-18A10 10 0 0 0 12 0zm0 14a4 4 0 1 1 0-8 4 4 0 0 1 0 8z"/></svg></span>
    <span>42 Ridgeline Way Carver Falls,<br>NV 89000</span>
  </div>
  <div class="fc" style="left:550px;top:136px;font-size:17px;font-weight:700">
    <span class="dot"><svg width="13" height="13" viewBox="0 0 24 24"><path fill="#f7941d" d="M6.6 10.8a15 15 0 0 0 6.6 6.6l2.2-2.2a1 1 0 0 1 1-.25 11.4 11.4 0 0 0 3.6.57 1 1 0 0 1 1 1V20a1 1 0 0 1-1 1A17 17 0 0 1 3 4a1 1 0 0 1 1-1h3.5a1 1 0 0 1 1 1c0 1.25.2 2.45.57 3.57a1 1 0 0 1-.25 1z"/></svg></span>
    555-014-2290
  </div>
  <div class="fc" style="left:550px;top:188px">
    <span class="dot"><svg width="13" height="10" viewBox="0 0 12 10"><rect x="0.5" y="0.5" width="11" height="9" fill="none" stroke="#f7941d"/><path d="M0.5 0.5 6 5 11.5 0.5" stroke="#f7941d" fill="none"/></svg></span>
    info@plinvaro.example
  </div>
  <h4 style="left:817px">Subscribe Now</h4>
  <p class="abs" style="left:817px;top:72px;width:272px;font-size:13px;line-height:18px">At vero eos et accusamus et iusto odio dignissimos ducimus qui blanditiis.</p>
  <div class="field" style="left:817px;top:121px;width:272px;height:40px;font-size:13px;gap:10px"><svg width="12" height="10" viewBox="0 0 12 10"><rect x="0.5" y="0.5" width="11" height="9" fill="none" stroke="#777"/><path d="M0.5 0.5 6 5 11.5 0.5" stroke="#777" fill="none"/></svg>Email Address</div>
  <a class="btn btn-orange" style="left:817px;top:172px;width:126px;height:38px;font-size:13px">Submit Now</a>
  <div class="fdivider"></div>
  <div class="copy">© 2022 Plinvaro LLC. Alle rechten voorbehouden</div>
</footer>

</body>
</html>
```